Bluestone Advisory & Mgmt - Professional Business Cards

Hi!

I am a Real Estate Developer and Construction Consultant.

I have a lot of inspiration from previous designs and would be open to using the attached Designs as a starting point. I would like to see these styles incorporated into your designs.

I really need professional business card to go with it that includes my important info.

Look forward to seeing your designs!.

Target Market(s)

My Target market are building owners, lawyers, consultants.

Industry/Entity Type

Real Estate Development

Contact Information for Business Card

My Name: Dorian Pelkey
My Title: Principle
Company Name: Bluestone Advisory & Mgmt, LLC
Address: 348 West 71st Street, 9th FL New York, NY 10010
Mobile: 917.806.3971
Website: bam-hvx.example

Font styles to use
Serif
Sans Serif

Colors

Designer to choose colors to be used in the design.

Requirements
Must have
• Must incorporate the logo attached or have new that looks similar.
• Must use professional font that will be seen and judged by wealthy land owners and developers.
• Must incorporate some of the color green.
Should not have
• Photo's or pictures of people or buildings of any kind.

```html
<!DOCTYPE html>
<html lang="en">
<head>
<meta charset="utf-8">
<title>Bluestone Advisory &amp; Mgmt - Business Cards</title>
<link rel="stylesheet" href="https://fonts.googleapis.com/css2?family=Raleway:wght@400&family=Didact+Gothic&display=swap">
<style>
  :root {
    --backdrop: #727071;
    --card-white: #ffffff;
    --blush-light: #dacdce;
    --blush-dark: #c4b7b8;
    --brand-green: #6fab74;
    --ink-white: #ffffff;
  }
  html, body {
    margin: 0;
    padding: 0;
    width: 1200px;
    height: 1200px;
    overflow: hidden;
    background: var(--backdrop);
  }
  .canvas {
    position: relative;
    width: 1200px;
    height: 1200px;
  }
  .card {
    position: absolute;
    left: 250px;
    width: 700px;
    height: 400px;
    background: var(--card-white);
  }
  .card--front { top: 147px; }
  .card--back { top: 652px; }

  .card__field {
    position: absolute;
    background: linear-gradient(100deg, var(--blush-light) 0%, var(--blush-dark) 100%);
  }
  .card--front .card__field { left: 16px; top: 16px; width: 653px; height: 369px; }
  .card--back .card__field { left: 12px; top: 16px; width: 658px; height: 357px; }

  .accent-bar {
    position: absolute;
    background: var(--brand-green);
  }
  .card--front .accent-bar--side { left: 669px; top: 16px; width: 14px; height: 369px; }
  .card--back .accent-bar--side { left: 670px; top: 16px; width: 15px; height: 369px; }
  .card--back .accent-bar--base { left: 12px; top: 373px; width: 673px; height: 12px; }

  .brand-name {
    position: absolute;
    right: 84px;
    top: 206px;
    margin: 0;
    font-family: "Raleway", sans-serif;
    font-weight: 400;
    color: var(--brand-green);
    text-align: left;
    line-height: 1;
  }
  .brand-name__main {
    display: block;
    font-size: 62px;
    letter-spacing: -1px;
  }
  .brand-name__sub {
    display: block;
    margin-top: 12px;
    font-size: 22px;
    letter-spacing: 0.5px;
  }

  .contact {
    position: absolute;
    left: 290px;
    top: 186px;
    font-family: "Didact Gothic", sans-serif;
    color: var(--ink-white);
    text-transform: uppercase;
    line-height: 1;
  }
  .contact p { margin: 0; }
  .contact__company { font-size: 18.5px; letter-spacing: 0.2px; }
  .contact__name { font-size: 15px; margin-top: 24px; }
  .contact__title { font-size: 15px; margin-top: 6px; }
  .contact__address { font-size: 14.5px; margin-top: 17px; letter-spacing: -0.2px; }
  .contact__phone { font-size: 14.5px; margin-top: 8px; }
  .contact__web { font-size: 15px; margin-top: 17px; }
</style>
</head>
<body>
<main class="canvas">
  <section class="card card--front" aria-label="Business card front">
    <div class="card__field"></div>
    <div class="accent-bar accent-bar--side"></div>
    <h1 class="brand-name">
      <span class="brand-name__main">Bluestone</span>
      <span class="brand-name__sub">Advisory Management</span>
    </h1>
  </section>

  <section class="card card--back" aria-label="Business card back">
    <div class="card__field"></div>
    <div class="accent-bar accent-bar--side"></div>
    <div class="accent-bar accent-bar--base"></div>
    <div class="contact">
      <p class="contact__company">Bluestone Advisory &amp; Mgmt, LLC</p>
      <p class="contact__name">Dorian Pelkey</p>
      <p class="contact__title">Principle</p>
      <p class="contact__address">348 West 71st Street, 9th FL New York, NY 10010</p>
      <p class="contact__phone">917.806.3971</p>
      <p class="contact__web">bam-hvx.example</p>
    </div>
  </section>
</main>
</body>
</html>
```